Design a Hemp Museum + exhibition design**

I'm creating an Online Museum for Hemp which will tell the story of hemp from ancient times to now and the future
cover the medical, industrial and nutritional uses and development of hemp
the people behind it, researchers, politicians, farmers and influencerts

the museum will have a number of "wings" , each holds an exhibition around a differnet theme, for example:

Hemp in the Age of Empires: 18th and 19th Century Collections
Hemp - The History of Healing
Domestication and Early Use: Ancient Collection
From Cotton Gin to Plastics and Prohibition: Hemp's Decline

these are just a few sample ideas for exhibitions

I'm looking for an overall design for the museum home page and exhibition page which will make people curious and want to spend time,learning and browsing

Think mobile -first :)

You are requested to design

1. Home page
2. Exhibition page

Target Market(s)

Hemp aficionados, curious fans

Logo Text

The Lumen Museum

Coding

Coded - Design and coding required

Number of Pages Required

3 page

Font styles to use
Sans Serif
Decorative

Requirements
Must have
• a homepage design which prompts visitors to immediately start watching an exhibition

visitors need to understand that this is a museum , so that they dont think it's a business, a service provider or anything like that

needs to have the usual links to T&C, privacy, about us

needs to have a link to "Wander past the lantern stall"

must have a visual WOW effect
Nice to have
• animations, sounds etc
Should not have
• forms like contact us etc - not relevant

```html
<!DOCTYPE html>
<html lang="en">
<head>
<meta charset="utf-8">
<title>The Lumen Museum</title>
<link rel="stylesheet" href="https://fonts.googleapis.com/css2?family=Prata&family=Jost:wght@400;500;600;700;800&display=swap">
<style>
:root{
  --green:#64a043;
  --green-title:#5b9a3e;
  --green-footer:#6aa84c;
  --ink:#1f1f1f;
  --body:#3a3a3a;
  --tan:#b89d6a;
  --frame:#e4e4e4;
  --white:#ffffff;
}
*{margin:0;padding:0;box-sizing:border-box}
html,body{width:1200px;height:3492px;overflow:hidden;background:var(--white)}
body{font-family:"Jost",sans-serif;color:var(--body)}
.page{position:relative;width:1200px;height:3492px}
.abs{position:absolute}

/* header */
.site-header{position:absolute;left:0;top:0;width:1200px;height:68px;background:var(--white)}
.brand{position:absolute;left:163px;top:17px;font-family:"Jost",sans-serif;font-weight:500;font-size:27px;color:var(--ink);line-height:1.2;display:flex;align-items:center;gap:10px}
.brand-dot{width:14px;height:14px;border-radius:50%;background:var(--green)}
.header-mail{position:absolute;left:689px;top:25px;font-size:15px;color:var(--ink);display:flex;align-items:center;gap:10px}
.header-menu{position:absolute;left:956px;top:26px;font-size:15px;font-weight:500;color:var(--ink);display:flex;align-items:center;gap:12px}

/* hero */
.hero{position:absolute;left:0;top:68px;width:1200px;height:510px;background:radial-gradient(ellipse at 50% 40%,#7a5838 0%,#4f3522 55%,#2c1d12 100%);text-align:center;color:var(--white)}
.hero-title{position:absolute;left:0;width:1200px;top:132px;font-family:"Jost",sans-serif;font-weight:800;font-size:55px;line-height:68px;letter-spacing:.5px}
.hero-sub{position:absolute;left:0;width:1200px;top:272px;font-size:20px;font-weight:500}
.hero-cta{position:absolute;left:494px;top:324px;width:214px;height:42px;border-radius:21px;background:var(--tan);color:var(--white);font-size:15px;font-weight:500;display:flex;align-items:center;justify-content:center;gap:8px}
.hero-notch{position:absolute;left:568px;top:480px;width:64px;height:64px;border-radius:50%;background:var(--white)}
.hero-notch span{position:absolute;left:23px;top:16px;width:18px;height:28px;border:2px solid var(--tan);border-radius:9px}

/* exhibits */
.exhibit-title{font-family:"Prata",serif;font-size:38px;line-height:49px;color:var(--green-title);font-weight:400}
.exhibit-kicker{font-family:"Prata",serif;font-size:24px;color:var(--ink)}
.exhibit-kicker sup{font-size:13px}
.exhibit-copy{font-size:15px;line-height:27px;color:var(--body)}
.exhibit-copy strong{color:var(--ink);font-weight:600}
.exhibit-copy p+p{margin-top:8px}
.btn{position:absolute;height:44px;background:var(--green);color:var(--white);font-size:15px;font-weight:500;display:flex;align-items:center;justify-content:center;letter-spacing:.3px}
.checklist{list-style:none;margin-top:14px}
.checklist li{display:flex;align-items:center;gap:10px;line-height:32px}

.frame{position:absolute;width:412px;height:345px}
.frame-back{position:absolute;top:0;width:358px;height:345px;border:3px solid var(--frame);background:var(--white)}
.frame-card{position:absolute;top:12px;width:393px;height:320px;background:var(--white);border:1px solid #ececec;box-shadow:0 2px 10px rgba(0,0,0,.12);padding:8px}
.frame-photo{width:100%;height:100%}
.frame--right .frame-back{left:54px}
.frame--right .frame-card{left:0}
.frame--left .frame-back{left:0}
.frame--left .frame-card{left:19px}

/* banner */
.explore{position:absolute;left:0;top:2833px;width:1200px;height:435px;background:linear-gradient(180deg,#3d4630 0%,#4d5a36 45%,#2d3720 100%);text-align:center;color:var(--white)}
.explore-title{position:absolute;left:0;width:1200px;top:66px;font-family:"Prata",serif;font-weight:400;font-size:38px;line-height:49px}
.explore-sub{position:absolute;left:0;width:1200px;top:186px;font-size:20px;font-weight:500}
.explore-copy{position:absolute;left:200px;width:800px;top:228px;font-size:15.5px;line-height:27px}
.explore .btn{left:457px;top:313px;width:285px;height:45px}

/* footer */
.site-footer{position:absolute;left:0;top:3268px;width:1200px;height:224px;background:var(--green-footer);color:var(--white);text-align:center}
.footer-brand{position:absolute;left:0;width:1200px;top:38px;font-family:"Jost",sans-serif;font-weight:500;font-size:31px}
.footer-links{position:absolute;left:0;width:1200px;top:85px;font-size:15px;display:flex;justify-content:center;gap:24px}
.footer-copy{position:absolute;left:0;width:1200px;top:116px;font-size:15px}
.footer-social{position:absolute;left:0;width:1200px;top:150px;display:flex;justify-content:center;gap:12px}
.footer-social span{width:30px;height:30px;border:2px solid var(--white);border-radius:50%}
</style>
</head>
<body>
<div class="page">

<header class="site-header">
  <div class="brand"><span class="brand-dot"></span>The Lumen Museum</div>
  <div class="header-mail">
    <svg width="18" height="13" viewBox="0 0 18 13"><rect x="0.5" y="0.5" width="17" height="12" fill="#64a043"/><path d="M1 1l8 6 8-6" stroke="#fff" stroke-width="1.4" fill="none"/></svg>
    inquiry@thelumenmuseum.com
  </div>
  <div class="header-menu">MENU
    <svg width="26" height="18" viewBox="0 0 26 18"><g stroke="#64a043" stroke-width="2"><line x1="0" y1="2" x2="26" y2="2"/><line x1="6" y1="9" x2="26" y2="9"/><line x1="0" y1="16" x2="26" y2="16"/></g></svg>
  </div>
</header>

<section class="hero" role="img" aria-label="Museum gallery room with framed engravings, a spinning wheel and a model sailing ship">
  <h1 class="hero-title">ONLINE HEMP<br>HISTORY MUSEUM</h1>
  <p class="hero-sub">We Are Hemp Aficionados, Curious Fans</p>
  <div class="hero-cta">
    <svg width="22" height="16" viewBox="0 0 22 16"><path d="M11 1v14M11 15L4 5M11 15l7-10M11 15L1 11M11 15l10-4" stroke="#fff" stroke-width="1.4" fill="none"/></svg>
    CONTACT US TODAY
  </div>
  <div class="hero-notch"><span></span></div>
</section>

<!-- Ancient Collection -->
<h2 class="exhibit-title abs" style="left:163px;top:628px">Ancient Collection</h2>
<div class="exhibit-copy abs" style="left:163px;top:696px;width:400px">
  <p><strong>Domestication and Early Use</strong> vivamus porttitor variustin turpis quis dapibus. Fusce congue arcu vel est hendrerit egestas ac vestibulum maximus mi ac erattan finibus, in consequat nulla ultricies.</p>
  <p>Aliquam tempus eros eu blandit egestas. Mauris ac urna nibh. Proin varius dui consectetur mi cursus, vitae sagitts quam volutpat praesent tincidunt mi at nisi.</p>
</div>
<div class="btn" style="left:161px;top:929px;width:150px">KNOW MORE</div>
<div class="frame frame--right" style="left:654px;top:633px">
  <div class="frame-back"></div>
  <div class="frame-card"><div class="frame-photo" role="img" aria-label="Engraving of people harvesting tall hemp plants by hand" style="background:linear-gradient(160deg,#e6e6e2,#a3a39e 60%,#6f6f6b)"></div></div>
</div>

<!-- 18th and 19th Century -->
<div class="frame frame--left" style="left:134px;top:1062px">
  <div class="frame-back"></div>
  <div class="frame-card"><div class="frame-photo" role="img" aria-label="Engraving of workers cutting and bundling hemp in a field" style="background:linear-gradient(180deg,#ededea,#b4b4af 55%,#5f5f5b)"></div></div>
</div>
<div class="exhibit-kicker abs" style="left:641px;top:1055px">18<sup>th</sup> And 19<sup>th</sup></div>
<h2 class="exhibit-title abs" style="left:641px;top:1096px">Century Collections</h2>
<div class="exhibit-copy abs" style="left:641px;top:1164px;width:405px">
  <p><strong>Hemp in the Age of Empires</strong> fermentum, lacus vi dictum luctus, dolor nibhet tristique ligula, nec pellentesque eros leo at lorem. Nulla sit amet odio sapien. Mauris tempus at elit sit amet rem scelerisque.</p>
  <p>Donec finibus, metus porta bibendum imperdiet, odiotort malesuada lectus, eu tincidunt ligula erat ut lectus sedm dolor enim, bibendum et facilisis et, tempus ac sem.</p>
</div>
<div class="btn" style="left:639px;top:1378px;width:149px">CONTACT US</div>

<!-- Hemp's Decline -->
<h2 class="exhibit-title abs" style="left:163px;top:1496px">Hemp's Decline</h2>
<div class="exhibit-copy abs" style="left:163px;top:1564px;width:405px">
  <p><strong>From Cotton Gin to Plastics and Prohibition</strong> aliquamete ante. Ut ut sagittis orci. In a metus eget fringilla rhoncus sed egestas ligula. Mauris id neque mauris. Nun aliquete elementum velit, quis sodales risus rutrum.</p>
  <p>Phasellus nisi purus, porttitor ac aliquam non, dictum in mattis libero. In id massa id orci aliquet lobortis at et mi. Duis porttitor metus at dignissim auctor.</p>
</div>
<div class="btn" style="left:161px;top:1780px;width:150px">KNOW MORE</div>
<div class="frame frame--right" style="left:654px;top:1502px">
  <div class="frame-back"></div>
  <div class="frame-card"><div class="frame-photo" role="img" aria-label="Freshly cut green hemp plants laid out on a work table" style="background:linear-gradient(180deg,#b9c3cc 0%,#8aa0a6 35%,#4d8a3a 65%,#2f5e25 100%)"></div></div>
</div>

<!-- Food, Textile and Biofuel -->
<div class="frame frame--left" style="left:134px;top:1926px">
  <div class="frame-back"></div>
  <div class="frame-card"><div class="frame-photo" role="img" aria-label="Jar of hemp seed oil beside a sack of seeds and a spoon of powder" style="background:linear-gradient(180deg,#6d7488 0%,#8a7a5e 45%,#c9a33a 60%,#5a4330 100%)"></div></div>
</div>
<h2 class="exhibit-title abs" style="left:641px;top:1918px">As A Food, Textile<br>And Biofuel</h2>
<div class="exhibit-copy abs" style="left:641px;top:2033px;width:405px">
  <p><strong>Hemp in Modern Industry</strong> fusce euismod fringilla neque eget venenatis. Nam eum tellus placerat, accumsan mit nec, vulputate quam. Proin imperdiet ornare ipsum. Inre rhoncus elit at erat ornare as vestibulum.</p>
  <p>Integer ornare nibh nec enim ullamcorper, vitae aliquam velit scelerisque. Nulla justo lectus, rutrum non urna euin, ornare blandit libero in eget lorem a quam lobortis.</p>
</div>
<div class="btn" style="left:639px;top:2244px;width:149px">KNOW MORE</div>

<!-- Medicine and Recreation -->
<h2 class="exhibit-title abs" style="left:163px;top:2353px">Cannabis As Modern<br>Medicine &amp; Recreation</h2>
<div class="exhibit-copy abs" style="left:163px;top:2468px;width:400px">
  <p><strong>The Green Revolution</strong> lacus vitae dictum luctus, doloret nibhm tristique ligula, nec pellentesque eros leo atlorem. Nulla sit amet odio sapien. Mauris tempus at elit sit ame sem scelerisque bibendum.</p>
  <ul class="checklist">
    <li><svg width="15" height="15" viewBox="0 0 15 15"><circle cx="7.5" cy="7.5" r="6.5" stroke="#64a043" stroke-width="1.3" fill="none"/><path d="M4.5 7.5l2.2 2.2 4-4.5" stroke="#64a043" stroke-width="1.4" fill="none"/></svg>Legalizing cannabis for medical application</li>
    <li><svg width="15" height="15" viewBox="0 0 15 15"><circle cx="7.5" cy="7.5" r="6.5" stroke="#64a043" stroke-width="1.3" fill="none"/><path d="M4.5 7.5l2.2 2.2 4-4.5" stroke="#64a043" stroke-width="1.4" fill="none"/></svg>Legalizing cannabis for recreation &amp; spiritual purposes</li>
    <li><svg width="15" height="15" viewBox="0 0 15 15"><circle cx="7.5" cy="7.5" r="6.5" stroke="#64a043" stroke-width="1.3" fill="none"/><path d="M4.5 7.5l2.2 2.2 4-4.5" stroke="#64a043" stroke-width="1.4" fill="none"/></svg>Legalizing cannabis for modern industrial application</li>
  </ul>
</div>
<div class="btn" style="left:161px;top:2705px;width:150px">KNOW MORE</div>
<div class="frame frame--right" style="left:654px;top:2361px">
  <div class="frame-back"></div>
  <div class="frame-card"><div class="frame-photo" role="img" aria-label="Doctor's hands holding a hemp leaf and a small medicine bottle" style="background:linear-gradient(160deg,#f1f2f2 0%,#d9dcdc 45%,#5f7a3a 60%,#e8e6e4 100%)"></div></div>
</div>

<section class="explore" role="img" aria-label="Field of flowering hemp plants at dusk">
  <h2 class="explore-title">Explore the World of Cannabis.<br>The Past, the Present &amp; the Future.</h2>
  <p class="explore-sub">Grand Exposition, Thinking Art Deco Modern World Fairs....</p>
  <p class="explore-copy">Nunc aliquet elementum velit, quis sodales risus rutrum id. Phasellus nisi purus, porttitor ac aliquam non, dictum mattis libero. In id massa id orci aliquet lobortis at et mi. Duis porttitor metus at dignissim auctor.</p>
  <div class="btn">WANDER PAST THE LANTERN STALL</div>
</section>

<footer class="site-footer">
  <div class="footer-brand">The Lumen Museum</div>
  <nav class="footer-links"><span>Terms &amp; Conditions</span><span>|</span><span>Privacy</span><span>|</span><span>About Us</span></nav>
  <p class="footer-copy">Copyright © 2021 The Lumen Museum. All Rights Reserved.</p>
  <div class="footer-social"><span></span><span></span><span></span></div>
</footer>

</div>
</body>
</html>
```